Business card: GREEN HERONS TRADE SUPPLY

Hello,

This is your mission:

-I've just done my logo on the website. Now, I need A BUSINESS CARD.
-2 same business cards for 2 persons
-Landscape
-Dimension of the business card: 8.5 cm long and 5 cm high
-Different front and back
-For your information: this new company is selling products (fashion accessories, electronics, watches, fragrances, sunglasses, etc. to large clients related to shops in airlines (inflight catalogue), airports, cruises, etc.
-Colors and logo: please use the same colors of the logo attached (in blue with orange details) and follow the spirit of the existing logo.

-Front:
-1st person:
GREEN HERONS s.p.r.l.
Travel Retail Agency
www.greenheronsx.com
Lucien DEMARBAIX
Partner
Mobile: +32488316257
Email: ld@greenheronsx.com
-2nd person:
GREEN HERONS s.p.r.l.
Travel Retail Agency
www.greenheronsx.com
Joris VANMECHELEN
Partner
Mobile: +32488625170
Email: jv@greenheronsx.com

-Back
Logo
see attached file. Please use the colors of the logo in blue with orange details.

Reason: I increase time necause i don t know if the deadline is in usa time or european time. I will make the selection at 9pm belgian time.

I'm selling products to large accounts/clients. Some of them do more than 2 Billion eur turnover

Airlines

Must have
• Use the logo.
The buyers get so many business cards.
They should remember me easily.
This is why my logo/company name is a stork and a color. 2 things that people usually remember easily.

```html
<!DOCTYPE html>
<html lang="en">
<head>
<meta charset="utf-8">
<title>Green Herons Trade Supply – Business Card</title>
<link rel="stylesheet" href="https://fonts.googleapis.com/css2?family=Open+Sans:wght@400;600&display=swap">
<style>
  :root {
    --backdrop: #d6d6d6;
    --card-white: #fbfbfb;
    --brand-navy: #0f4a86;
    --brand-teal: #1f9bb8;
    --brand-orange: #f28a1c;
    --text-dark: #2e2e2e;
    --text-grey: #6a6a6a;
  }
  * { margin: 0; padding: 0; box-sizing: border-box; }
  html, body { width: 1200px; height: 750px; overflow: hidden; }
  body {
    background: var(--backdrop);
    font-family: "Open Sans", Arial, sans-serif;
    position: relative;
  }
  .card {
    position: absolute;
    width: 425px;
    height: 250px;
    background: var(--card-white);
    border-radius: 16px;
    overflow: hidden;
    box-shadow: 0 4px 10px rgba(0,0,0,0.12);
  }
  .card-back { left: 150px; top: 130px; }
  .card-front { left: 625px; top: 370px; }
  .card-art { position: absolute; inset: 0; }

  .company-name {
    position: absolute;
    color: var(--brand-navy);
    font-weight: 600;
    line-height: 1.2;
    white-space: nowrap;
    display: flex;
    align-items: center;
    gap: 8px;
  }
  .company-dot {
    width: 10px; height: 10px;
    border-radius: 50%;
    background: var(--brand-orange);
    flex: none;
  }
  .card-back .company-name { left: 76px; top: 112px; font-size: 17px; }
  .card-front .company-name { left: 58px; top: 80px; font-size: 13px; }

  .web-strip {
    position: absolute;
    left: 0; top: 0; bottom: 0;
    width: 28px;
    background: var(--brand-teal);
  }
  .web-address {
    position: absolute;
    left: 19px; bottom: 14px;
    transform: rotate(-90deg);
    transform-origin: left center;
    white-space: nowrap;
    color: #fff;
    font-size: 11px;
  }
  .top-band {
    position: absolute;
    left: 190px; right: 0; top: 18px;
    height: 48px;
    background: var(--brand-navy);
  }
  .contact-box {
    position: absolute;
    left: 235px; right: 0; top: 112px;
    height: 56px;
    background: var(--brand-navy);
    border-radius: 14px 0 0 14px;
    color: #fff;
    font-size: 12px;
    padding: 10px 0 0 14px;
    line-height: 1.45;
  }
  .contact-icons {
    position: absolute;
    left: 212px; top: 122px;
    display: flex; flex-direction: column; gap: 6px;
  }
  .contact-icon {
    width: 15px; height: 15px;
    border-radius: 50%;
    background: var(--brand-orange);
    display: flex; align-items: center; justify-content: center;
  }
  .person {
    position: absolute;
    left: 108px; top: 180px;
    color: var(--text-dark);
    font-size: 15px;
    line-height: 1.2;
  }
  .person .role {
    display: block;
    color: var(--text-grey);
    font-size: 12px;
    text-align: right;
  }
</style>
</head>
<body>

  <section class="card card-back" aria-label="Card back">
    <svg class="card-art" viewBox="0 0 425 250" aria-hidden="true">
      <rect x="60" y="55" width="330" height="125" rx="14" fill="none" stroke="var(--brand-teal)" stroke-width="4"/>
      <line x1="0" y1="150" x2="62" y2="150" stroke="var(--brand-teal)" stroke-width="4"/>
      <path d="M0 152 H290 a18 18 0 0 1 18 18 V250 H0 Z" fill="var(--brand-navy)"/>
    </svg>
    <div class="company-name"><span class="company-dot"></span><span>GREEN HERONS TRADE SUPPLY</span></div>
  </section>

  <section class="card card-front" aria-label="Card front">
    <div class="web-strip"><span class="web-address">www.greenheronsx.com</span></div>
    <div class="top-band"></div>
    <div class="company-name"><span>GREEN HERONS TRADE SUPPLY</span></div>
    <div class="contact-icons">
      <span class="contact-icon">
        <svg width="9" height="9" viewBox="0 0 10 10" aria-label="Mobile"><rect x="2.5" y="0.5" width="5" height="9" rx="1" fill="none" stroke="#fff" stroke-width="1.2"/></svg>
      </span>
      <span class="contact-icon">
        <svg width="9" height="9" viewBox="0 0 10 10" aria-label="Email"><rect x="0.8" y="2" width="8.4" height="6" fill="none" stroke="#fff" stroke-width="1.1"/><path d="M1 2.3 L5 5.5 L9 2.3" fill="none" stroke="#fff" stroke-width="1.1"/></svg>
      </span>
    </div>
    <div class="contact-box">
      <div>+32488316257</div>
      <div>ld@greenheronsx.com</div>
    </div>
    <div class="person">
      Lucien<br>DEMARBAIX
      <span class="role">Partner</span>
    </div>
  </section>

</body>
</html>
```